KTRV Promo Flyer for Corporate Events

Need a 8 page company overview

Target Market(s)

Creditors and Service Providers

Industry/Entity Type

Credit Card

Font styles to use
Serif

Colors
0455a3
fbf289

Requirements
Must have
• Fantastic Material and Creative
Nice to have
• Creative and personal

```html
<!DOCTYPE html>
<html lang="en">
<head>
<meta charset="utf-8">
<title>KTRV Recovery Bureau – Company Overview</title>
<link href="https://fonts.googleapis.com/css2?family=Libre+Baskerville:wght@400;700&family=Lora:ital,wght@0,400;0,700;1,400&display=swap" rel="stylesheet">
<style>
:root{
  --blue:#0455a3;
  --blue-dark:#033e78;
  --yellow:#fbf289;
  --gold:#f2c640;
  --stage:#a3a3a3;
  --paper:#ffffff;
  --ink:#2b2b2b;
  --muted:#6a7280;
}
*{box-sizing:border-box;margin:0;padding:0}
html,body{width:1200px;height:3600px;overflow:hidden}
body{background:var(--stage);position:relative;font-family:"Lora",Georgia,serif;color:var(--ink)}
.page-no{position:absolute;font:700 44px "Libre Baskerville",Georgia,serif;color:#111}
.page{position:absolute;width:380px;height:580px;overflow:hidden;background:var(--paper);box-shadow:0 4px 12px rgba(0,0,0,.35)}
.page.blue{background:var(--blue);color:#fff}
.page.yellow{background:var(--yellow)}
.band-top{position:absolute;left:0;top:0;width:100%;height:8px;background:var(--gold)}
.band-bottom{position:absolute;left:0;bottom:0;width:100%;height:14px;background:var(--blue);border-top:5px solid var(--gold)}
.blue .band-bottom{background:var(--gold);border-top:5px solid var(--blue-dark)}
.photo{position:absolute}
h2{font:700 13px "Libre Baskerville",Georgia,serif;color:var(--blue);line-height:1.2}
.blue h2{color:var(--yellow)}
h3{font:700 9.5px "Libre Baskerville",Georgia,serif;color:var(--blue);margin-top:4px}
.blue h3{color:var(--yellow)}
p,li{font-size:7px;line-height:1.45}
ul{padding-left:12px}
.wordmark{font:700 19px "Libre Baskerville",Georgia,serif;color:var(--blue);letter-spacing:.5px;display:flex;align-items:center;gap:8px}
.wordmark .dot{width:12px;height:12px;border-radius:50%;background:var(--gold)}
.tagline{font:italic 9px "Lora",serif;color:var(--muted);margin-top:3px}
.url-chip{display:inline-block;background:var(--blue);color:#fff;font-size:7px;padding:3px 10px;margin-top:10px}
.content{position:absolute;left:22px;right:22px}
.ribbon{background:var(--yellow);color:var(--blue);font:700 11px "Libre Baskerville",serif;text-align:center;padding:5px 0;border-radius:3px}
.partner{width:52px;height:16px;border-radius:3px;background:#c9d6e6}
.grid4{display:grid;grid-template-columns:1fr 1fr;gap:10px 14px}
.tile h3{margin-bottom:4px}
.tile .img{height:70px}
.badge{width:60px;height:34px;border-radius:4px}
</style>
</head>
<body>

<!-- Page 1: front cover -->
<div class="page-no" style="left:300px;top:330px">1</div>
<section class="page cover" style="left:400px;top:60px">
  <div class="band-top"></div>
  <div class="photo" role="img" aria-label="City skyline with observation tower under a blue sky" style="left:0;top:8px;width:380px;height:340px;background:linear-gradient(180deg,#4e86c9 0%,#8fb3dc 45%,#5b6f86 75%,#6f8a4c 100%)"></div>
  <div class="content" style="top:400px">
    <div class="wordmark"><span class="dot"></span>KTRV RECOVERY BUREAU</div>
    <div class="tagline">Accounts Receivable Management</div>
    <span class="url-chip">www.ktrv-example.net</span>
  </div>
  <div class="band-bottom"></div>
</section>

<!-- Page 2 -->
<div class="page-no" style="left:40px;top:1000px">2</div>
<section class="page blue" style="left:100px;top:740px">
  <div class="content" style="top:22px">
    <h2>Mission Statement</h2>
    <h3>Our Mission Is Simple</h3>
    <p>We are a recovery partner built on trust. Every account is handled with care, accuracy and respect for the consumer and the client.</p>
    <h3>Our Vision Is Simple</h3>
    <p>To be the most reliable receivables partner in the region, delivering strong results through ethical practice and clear communication.</p>
    <div class="ribbon" style="margin:14px 0 8px">How Collections Works</div>
    <svg width="336" height="256" viewBox="0 0 336 256">
      <circle cx="168" cy="120" r="88" fill="none" stroke="#fff" stroke-width="2" stroke-dasharray="6 5"/>
      <g fill="var(--yellow)">
        <circle cx="168" cy="32" r="16"/><circle cx="254" cy="92" r="16"/><circle cx="222" cy="196" r="16"/>
        <circle cx="114" cy="196" r="16"/><circle cx="82" cy="92" r="16"/>
      </g>
      <text x="168" y="116" fill="#fff" font-family="Libre Baskerville,serif" font-size="11" font-weight="700" text-anchor="middle">KTRV Recovery Bureau</text>
      <text x="168" y="131" fill="#fff" font-family="Lora,serif" font-size="8" text-anchor="middle">Accounts Receivable Management</text>
      <g fill="#fff" font-family="Lora,serif" font-size="7" text-anchor="middle">
        <circle cx="40" cy="232" r="10" fill="var(--yellow)"/><text x="40" y="252">Placement</text>
        <circle cx="130" cy="232" r="10" fill="var(--yellow)"/><text x="130" y="252">Contact</text>
        <circle cx="210" cy="232" r="10" fill="var(--yellow)"/><text x="210" y="252">Resolution</text>
        <circle cx="296" cy="232" r="10" fill="var(--yellow)"/><text x="296" y="252">Remittance</text>
      </g>
    </svg>
  </div>
  <div class="band-bottom"></div>
</section>

<!-- Page 3 -->
<div class="page-no" style="left:1130px;top:1000px">3</div>
<section class="page" style="left:680px;top:740px">
  <div class="band-top"></div>
  <div class="content" style="top:24px">
    <h2>The KTRV Difference</h2>
    <p>Our team pairs experienced collectors with modern tools. We work each account personally and keep clients informed at every step of the process.</p>
    <h2 style="margin-top:12px">Our Affiliations</h2>
    <div style="display:flex;justify-content:space-between;margin:8px 0 12px">
      <div class="partner"></div><div class="partner"></div><div class="partner"></div><div class="partner"></div><div class="partner"></div>
    </div>
    <h2>Acquisition Summary</h2>
    <p>Founded as a regional agency, the firm has grown through steady investment in people and systems. Today it serves creditors and service providers across many industries with the same personal focus it began with.</p>
    <h2 style="margin-top:12px">Key Components</h2>
    <ul>
      <li>Licensed and bonded in every state we serve</li>
      <li>Secure data handling and regular audits</li>
      <li>Dedicated client relations staff</li>
    </ul>
    <h2 style="margin-top:12px">Brand Vision</h2>
    <ul>
      <li>Consistently deliver measurable results</li>
      <li>Treat every consumer with dignity</li>
      <li>Build long-term client partnerships</li>
    </ul>
  </div>
  <div class="band-bottom"></div>
</section>

<!-- Page 4 -->
<div class="page-no" style="left:40px;top:1740px">4</div>
<section class="page" style="left:100px;top:1480px">
  <div class="band-top"></div>
  <div class="content" style="top:26px">
    <div class="grid4">
      <div class="tile"><h3>Outstanding Consumer Relations</h3><div class="img" role="img" aria-label="Call center agent with headset" style="background:linear-gradient(135deg,#3a6fa8,#9cc0e0)"></div></div>
      <div class="tile"><h3>Responsive Client Service</h3><div class="img" role="img" aria-label="Group of business people illustration" style="background:linear-gradient(135deg,#dfe7ef,#8aa7c4)"></div></div>
      <div class="tile"><h3>Customized Management Reporting</h3><div class="img" role="img" aria-label="Communication concept on a board" style="background:linear-gradient(135deg,#e8d9b4,#9a7e4c)"></div></div>
      <div class="tile"><h3>Complete Compliance</h3><div class="img" role="img" aria-label="Compliance checklist with gavel" style="background:linear-gradient(135deg,#f1f1f1,#a8b0bb)"></div></div>
    </div>
    <div style="width:170px;margin:16px auto 0" class="tile">
      <h3 style="text-align:center">Highly Effective Data Security</h3>
      <div class="img" role="img" aria-label="Digital padlock on a dark circuit background" style="height:80px;background:linear-gradient(135deg,#0c1f3a,#2f5c8f)"></div>
    </div>
  </div>
  <div class="band-bottom"></div>
</section>

<!-- Page 5 -->
<div class="page-no" style="left:1130px;top:1740px">5</div>
<section class="page yellow" style="left:680px;top:1480px">
  <div class="content" style="top:20px">
    <div style="display:flex;gap:12px">
      <div style="flex:1">
        <h2>Leadership</h2>
        <h3>Key Personnel</h3>
        <h3>Martin Hale</h3>
        <p>Chief Executive Officer</p>
      </div>
      <div role="img" aria-label="Insights concept with magnifying glass" style="width:150px;height:78px;background:linear-gradient(135deg,#ffffff,#9fb8d4)"></div>
    </div>
    <p style="margin-top:8px">Martin leads strategy and client partnerships, guiding the company with a focus on results, fairness and steady growth.</p>
    <h2 style="margin-top:10px">E Accessibility</h2>
    <p>Clients reach their accounts online at any hour.</p>
    <ul>
      <li>Client Dashboard</li><li>Real-Time Account Status</li><li>Online Payments</li><li>Document Upload</li><li>Secure Messaging</li>
    </ul>
    <div style="display:flex;gap:10px;margin-top:8px">
      <div style="flex:1">
        <h3>Service Capabilities</h3>
        <ul><li>Early-Out Programs</li><li>Bad Debt Recovery</li><li>Skip Tracing</li><li>Litigation Support</li><li>Payment Plans</li><li>Custom Reporting</li></ul>
      </div>
      <div role="img" aria-label="Airplane over a globe illustration" style="width:150px;height:90px;background:linear-gradient(135deg,#dbe8f5,#5f8fc4)"></div>
    </div>
    <h2 style="margin-top:10px">Key Personnel</h2>
    <h3>Owen Riley</h3>
    <p>Chief Executive Officer. Owen brings many years of recovery experience and oversees daily operations across every client program we manage.</p>
  </div>
</section>

<!-- Page 6 -->
<div class="page-no" style="left:40px;top:2490px">6</div>
<section class="page blue" style="left:100px;top:2230px">
  <div class="content" style="top:24px">
    <h2>Owen Riley</h2><h3>Chief Financial Officer</h3>
    <p>Owen manages finance, trust accounting and audit readiness, ensuring every remittance is accurate and delivered on schedule to our clients.</p>
    <h2 style="margin-top:14px">Grant Ellison</h2><h3>Director of Operations</h3>
    <p>Grant directs the collection floor and training. His teams pair careful listening with firm follow-through to resolve accounts.</p>
    <h2 style="margin-top:14px">Laura Penn</h2><h3>Client Services Manager</h3>
    <p>Laura is the main point of contact for clients, building custom reports and keeping each program aligned with client goals.</p>
    <h2 style="margin-top:14px">Nora Walsh</h2><h3>Compliance Officer</h3>
    <p>Nora maintains our licensing, policies and audits so that every call and letter meets state and federal requirements.</p>
  </div>
  <div class="band-bottom"></div>
</section>

<!-- Page 7 -->
<div class="page-no" style="left:1130px;top:2490px">7</div>
<section class="page" style="left:680px;top:2230px">
  <div class="band-top"></div>
  <div class="content" style="top:22px">
    <h2>Our Values</h2>
    <div style="display:flex;justify-content:space-between;margin:8px 0">
      <div class="badge" style="background:#f4a93b"></div>
      <div class="badge" style="background:#e2517a"></div>
      <div class="badge" style="background:#2d2d2d;border-radius:50%;width:38px;height:38px"></div>
    </div>
    <div style="display:flex;justify-content:space-between">
      <div class="badge" style="background:#8fc1e3"></div>
      <div class="badge" style="background:#e65a3a"></div>
      <div class="badge" style="background:#3f9a4d"></div>
    </div>
  </div>
  <div class="photo" role="img" aria-label="Snow-capped mountain rising behind a city skyline" style="left:0;top:150px;width:380px;height:230px;background:linear-gradient(180deg,#e8b27b 0%,#c98a6a 40%,#7c6a7e 70%,#2e3346 100%)"></div>
  <div class="content" style="top:396px">
    <h2>The KTRV Difference</h2>
    <h3>Quality and Excellence</h3>
    <p>We measure success by the trust we earn. Our people, processes and technology work together to deliver dependable recovery and a respectful experience for every consumer.</p>
    <p style="margin-top:6px">Thank you for considering our team as your partner.</p>
  </div>
  <div class="band-bottom"></div>
</section>

<!-- Page 8: back cover -->
<div class="page-no" style="left:300px;top:3260px">8</div>
<section class="page" style="left:400px;top:2990px">
  <div class="band-top"></div>
  <div class="photo" role="img" aria-label="City skyline at dusk with water in the foreground" style="left:0;top:8px;width:380px;height:300px;background:linear-gradient(180deg,#3a6aa8 0%,#6f95c4 45%,#3b4a66 80%,#1f2f4a 100%)"></div>
  <div class="content" style="top:330px;text-align:center">
    <div class="wordmark" style="justify-content:center"><span class="dot"></span>KTRV RECOVERY BUREAU</div>
    <div class="tagline">Accounts Receivable Management</div>
    <h3 style="margin-top:90px">Your Receivables Management Partner</h3>
    <p style="margin-top:6px">4100 Harbor Lane, Suite 210<br>Lakeview, WA 98000</p>
    <p>(555) 010-2040</p>
    <p>www.ktrv-example.net</p>
  </div>
  <div class="band-bottom"></div>
</section>

</body>
</html>
```